Email Signature

We want a new email signature designed that will include an employees picture and our logo at minimum. Of course contact info as well.

For the sample please create the new signature for Dale Prewitt...extra pics provided
please visit our website www.BrightwayUpkeep.com

Need to limit links to our website....government email servers strip out many.
Updates

I have a new draft design I'd like to work from...simple and clean.Needs:LogoDisclaimerand a bit of colorI'd like to make selection this week. Added Tuesday, October 24, 2017

Target Market(s)

other professional businesses

Requirements
Must have
• picture & Logo
• new look and something that auto scales to the emails window.
• Would like to have a new tag line "

```html
<!DOCTYPE html>
<html lang="en">
<head>
<meta charset="utf-8">
<title>Email Signature – Dale Prewitt</title>
<link rel="stylesheet" href="https://fonts.googleapis.com/css2?family=Lato:wght@400;700&display=swap">
<style>
  :root {
    --page-bg: #ffffff;
    --ink: #1f1f1f;
    --ink-soft: #333333;
    --ink-muted: #7a7a7a;
    --accent: #55aaf0;
    --rule: #9a9a9a;
    --photo-light: #d9d4d0;
    --photo-dark: #5a5450;
  }
  * { box-sizing: border-box; margin: 0; padding: 0; }
  html, body {
    width: 1200px;
    height: 947px;
    overflow: hidden;
    background: var(--page-bg);
    font-family: "Lato", Arial, sans-serif;
    color: var(--ink);
  }
  .signature-block {
    position: absolute;
    left: 60px;
    top: 200px;
    width: 1080px;
  }
  .signature {
    display: flex;
    align-items: flex-start;
  }
  .signature__photo {
    width: 186px;
    height: 186px;
    margin-top: 16px;
    border-radius: 50%;
    background: radial-gradient(circle at 50% 40%, var(--photo-light) 0%, #b9aea6 45%, var(--photo-dark) 100%);
    flex-shrink: 0;
  }
  .signature__details {
    margin-left: 30px;
    padding-left: 22px;
    border-left: 6px solid var(--accent);
    width: 800px;
    padding-bottom: 4px;
  }
  .signature__name {
    font-size: 24px;
    font-weight: 700;
    line-height: 1.25;
  }
  .signature__role,
  .signature__company {
    font-size: 19px;
    line-height: 1.35;
    color: var(--ink-soft);
  }
  .signature__divider {
    width: 720px;
    margin: 16px 0 10px;
    border: 0;
    border-top: 2px dashed var(--rule);
  }
  .signature__address {
    font-size: 20px;
    line-height: 1.5;
    color: var(--ink-soft);
  }
  .signature__phones {
    font-size: 17px;
    line-height: 1.7;
    color: var(--ink-soft);
  }
  .signature__web {
    font-size: 20px;
    line-height: 1.6;
    color: var(--ink-soft);
  }
  .signature__web a {
    color: var(--accent);
    text-decoration: none;
  }
  .signature__social {
    display: flex;
    gap: 5px;
    margin-top: 6px;
  }
  .signature__social span {
    width: 24px;
    height: 24px;
    border-radius: 50%;
    background: var(--accent);
    opacity: 0.85;
  }
  .brand {
    display: flex;
    align-items: center;
    gap: 10px;
    margin-top: 22px;
  }
  .brand__mark {
    width: 26px;
    height: 26px;
    border-radius: 50%;
    background: var(--accent);
  }
  .brand__name {
    font-size: 22px;
    font-weight: 700;
    color: var(--accent);
  }
  .brand__tagline {
    margin-top: 6px;
    font-size: 17px;
    font-style: italic;
    color: var(--ink-soft);
  }
  .disclaimer {
    margin-top: 34px;
    padding-top: 12px;
    border-top: 1px solid #dddddd;
    font-size: 13px;
    line-height: 1.5;
    color: var(--ink-muted);
  }
</style>
</head>
<body>
  <section class="signature-block">
    <div class="signature">
      <div class="signature__photo" role="img" aria-label="Portrait photo of Dale Prewitt"></div>
      <div class="signature__details">
        <p class="signature__name">Dale Prewitt</p>
        <p class="signature__role">Director of Pre-Construction</p>
        <p class="signature__company">Brightway Upkeep Inc.</p>
        <hr class="signature__divider">
        <p class="signature__address">450 Harbor Lane, Oakridge, CA 94012</p>
        <p class="signature__phones">C. 415-555-0161 | O. 800-555-0173 x206 | F. 800-555-0174</p>
        <p class="signature__web">e. <a href="#">DPrewitt@BrightwayUpkeep.com</a> &nbsp;| w. <a href="#">www.BrightwayUpkeep.com</a></p>
        <div class="signature__social" aria-label="Social links">
          <span></span><span></span><span></span>
        </div>
        <div class="brand">
          <span class="brand__mark"></span>
          <span class="brand__name">Brightway Upkeep</span>
        </div>
        <p class="brand__tagline">Keeping your spaces bright, safe and running.</p>
      </div>
    </div>
    <p class="disclaimer">This message and any attachments are confidential and intended only for the named recipient. If you received it in error, please notify the sender and delete it. Any unauthorized review, use or distribution is prohibited.</p>
  </section>
</body>
</html>
```